New website

We ned to create a new website that reflects more who we are. We are delivering exclusive premium products to our customers and the current website does not reflect our products at all.
We believe in less is more and need a webpage that is clean yet professional and exclusive.

Target Market(s)

Dentistry

Industry/Entity Type

Dental

Number of Pages Required

5+ page

Font styles to use
Sans Serif

Colors

Designer to choose colors to be used in the design.

Requirements
Must have
• Picture gallery
• Nice structure
• Clean layout
Nice to have
• Light fonts
Should not have
• Any italic font styles

```html
<!DOCTYPE html>
<html lang="sv">
<head>
<meta charset="utf-8">
<title>Lumadent – Välkommen</title>
<link href="https://fonts.googleapis.com/css2?family=Lato:wght@300;400;700;900&display=swap" rel="stylesheet">
<style>
  :root {
    --brand-blue: #0b5fa8;
    --bar-blue: #1b6fb5;
    --brand-red: #e3182d;
    --badge-yellow: #f5d10a;
    --ink: #2b2b2b;
    --muted: #7a7a7a;
    --line: #d9d9d9;
    --paper: #ffffff;
  }
  * { box-sizing: border-box; margin: 0; padding: 0; }
  html, body { width: 1200px; height: 607px; overflow: hidden; }
  body { font-family: "Lato", sans-serif; color: var(--ink); background: var(--paper); }
  .site { width: 1200px; height: 607px; display: flex; flex-direction: column; }

  .topbar { height: 26px; flex: none; background: var(--bar-blue); color: #fff; font-size: 10px; font-weight: 700;
    letter-spacing: .04em; position: relative; display: flex; align-items: center; z-index: 2; }
  .topbar__book { position: absolute; right: 640px; }
  .topbar__badge { position: absolute; left: 568px; top: 0; width: 34px; height: 36px; background: var(--badge-yellow);
    color: var(--ink); font-size: 9px; font-weight: 900; text-align: center; padding-top: 6px;
    clip-path: polygon(0 0,100% 0,100% 78%,50% 100%,0 78%); }
  .topbar__lang { position: absolute; right: 160px; display: flex; align-items: center; gap: 6px; }
  .topbar__lang .flag { width: 14px; height: 9px; background: #fff; border: 2px solid var(--brand-red); display: inline-block; }

  .header { height: 72px; flex: none; display: flex; align-items: flex-end; justify-content: center; padding-bottom: 14px;
    background: linear-gradient(#fafafa, #f0f0f0); }
  .logo__name { font-weight: 400; font-size: 24px; color: var(--ink); }

  .nav { height: 34px; flex: none; border-top: 1px solid var(--line); border-bottom: 1px solid #e6b4b9;
    background: #f7f7f7; display: flex; justify-content: center; gap: 56px; align-items: stretch; }
  .nav a { font-size: 13px; color: #444; text-decoration: none; display: flex; align-items: center; }
  .nav a.is-active { border-bottom: 2px solid var(--brand-red); }
  .nav a.is-faint { color: #999; }

  .hero { position: relative; height: 200px; flex: none; }
  .hero__photo { position: absolute; inset: 0;
    background: linear-gradient(90deg, #e9e9e9 0%, #eeeeee 45%, #e2d6cf 62%, #d9c8bd 75%, #cfd3e6 90%, #e6e6e6 100%); }
  .hero__copy { position: absolute; left: 250px; top: 80px; }
  .hero__title { color: var(--brand-red); font-weight: 900; font-size: 24px; }
  .hero__sub { font-size: 17px; color: var(--ink); margin-top: 2px; }

  .products { background: var(--brand-blue); height: 48px; flex: none; color: #fff; text-align: center; font-size: 12px;
    font-weight: 700; letter-spacing: .04em; padding-top: 9px; }
  .products__row { background: var(--paper); height: 56px; flex: none; display: flex; justify-content: center; gap: 46px; }
  .products__btn { margin-top: -18px; width: 118px; height: 40px; background: #fff; border: 1px solid #cfcfcf;
    box-shadow: 0 3px 5px rgba(0,0,0,.18); font-size: 12px; display: flex; align-items: center; justify-content: center; color: #333; }

  .intro { flex: 1; background: linear-gradient(90deg, #f4f4f4, #f1efee 60%, #f6f6f6); padding: 20px 0 0 252px; display: flex; gap: 26px; }
  .intro__media { display: flex; flex-direction: column; gap: 4px; }
  .intro__photo { width: 258px; height: 96px; background: linear-gradient(120deg, #c9b7ad, #e8ddd7 55%, #f3efec); }
  .intro__thumbs { display: flex; gap: 4px; }
  .intro__thumbs i { width: 50px; height: 14px; background: #cfcfcf; display: block; }
  .intro__thumbs i:first-child { background: var(--brand-red); }
  .intro__text { width: 380px; }
  .intro__title { font-size: 21px; font-weight: 400; margin-bottom: 6px; }
  .intro__body { font-size: 11px; color: var(--muted); line-height: 1.45; }
  .intro__link { font-size: 11px; color: var(--brand-red); margin: 6px 0; }
  .intro__more { display: inline-block; background: var(--brand-blue); color: #fff; font-size: 10px; padding: 4px 10px; }
</style>
</head>
<body>
<div class="site">
  <div class="topbar">
    <span class="topbar__book">BOKA ETT MÖTE ONLINE</span>
    <span class="topbar__badge">NU</span>
    <span class="topbar__lang">ENGLISH <span class="flag"></span></span>
  </div>

  <header class="header">
    <div class="logo__name">Lumadent</div>
  </header>

  <nav class="nav">
    <a href="#" class="is-active">Välkommen</a>
    <a href="#">Produkter</a>
    <a href="#">Tjänster</a>
    <a href="#">Leenden</a>
    <a href="#" class="is-faint">Om Lumadent</a>
    <a href="#" class="is-faint">Kontakt</a>
  </nav>

  <section class="hero">
    <div class="hero__photo" role="img" aria-label="Foto: leende kvinna i tandläkarstol som gör tummen upp"></div>
    <div class="hero__copy">
      <div class="hero__title">Lumadent gör Sverige vackrare,</div>
      <div class="hero__sub">ett leende i taget!</div>
    </div>
  </section>

  <div class="products">VÅRA PRODUKTER</div>
  <div class="products__row">
    <div class="products__btn">Estetik &amp; Funktion</div>
    <div class="products__btn">Helkeramik</div>
    <div class="products__btn">Diagnostik</div>
    <div class="products__btn">Implantat</div>
    <div class="products__btn">Plåster</div>
  </div>

  <section class="intro">
    <div class="intro__media">
      <div class="intro__photo" role="img" aria-label="Foto: närbild av leende med tandinstrument"></div>
      <div class="intro__thumbs"><i></i><i></i><i></i></div>
    </div>
    <div class="intro__text">
      <h2 class="intro__title">Vi skapar leenden</h2>
      <p class="intro__body">Lumadent är specialiserat på keramiska och estetiska lösningar för tandvården. Vi levererar premiumprodukter till kliniker och laboratorier som vill ge sina patienter ett naturligt och hållbart leende.</p>
      <p class="intro__link">Våra leenden talar för sig själva, se fler i vårt galleri</p>
      <span class="intro__more">Läs mer</span>
    </div>
  </section>
</div>
</body>
</html>
```